From Portrait to Landscape

Take a PPT document made of 54 slide of graphs, images and text and change the orientation of each one of the 54 slides from the existing Portrait layout to the Landscape one.
All the graphics and texts (including text formatting, commas, bullet points etc.) must be kept the same but spaces are reorganized in the new Landscape orientation favoring the size of the graphs (possibily reducing the text areas).
Please, find attached the first 10 pages of the PPT document (for now, in PDF format) and a couple of sample pages of the PPT.x\

Target Market(s)

Readers of the Report (ecommerce players in Italy)

Requirements
Must have
• Graphics should be larger in the Landscape orientation than they are now in the Poirtrait one

```html
<!DOCTYPE html>
<html lang="it">
<head>
<meta charset="utf-8">
<title>Retail Online – Aprile 2022</title>
<link href="https://fonts.googleapis.com/css2?family=Alegreya+Sans:wght@400;500;700&display=swap" rel="stylesheet">
<style>
:root{
  --page:#7f7f7e; --white:#ffffff; --navy:#1f2a5c; --olive:#7a8a47; --olive-dark:#5f6d34;
  --lime:#a6ae3e; --lime-pale:#e7e8c9; --orange:#e07b2a; --teal:#6cc4bc; --pink:#e05a7a;
  --blue:#1c56a6; --red:#d8333f; --yellow:#f2b52a; --dgray:#4d4d4d; --mgray:#7c7c7c;
  --lgray:#e6e6e6; --brown:#7b6e5e; --ink:#4a4a4a; --rule:#6b7a3a;
}
*{box-sizing:border-box;margin:0;padding:0}
html,body{width:901px;height:1200px;overflow:hidden;background:var(--page)}
body{position:relative;font-family:"Alegreya Sans",sans-serif;color:var(--ink)}
.slide{position:absolute;width:370px;height:210px;background:var(--white);overflow:hidden}
.col-l{left:77px}.col-r{left:457px}
.row1{top:54px}.row2{top:273px}.row3{top:491px}.row4{top:709px}.row5{top:927px}
.abs{position:absolute}
.title{position:absolute;left:34px;top:15px;font-size:9.5px;font-weight:700;color:var(--olive-dark);letter-spacing:.1px}
.title-rule{position:absolute;left:34px;width:303px;top:27px;height:1px;background:var(--rule)}
.subtitle{position:absolute;left:34px;top:30px;font-size:7.6px;color:var(--olive-dark)}
.footer{position:absolute;left:34px;width:303px;top:191px;height:8px;background:var(--olive);color:#fff;font-size:6px;line-height:8px;padding:0 8px;display:flex;justify-content:space-between}
.body-text{font-size:3.4px;line-height:4.2px;color:#555;text-align:justify}
.caption{position:absolute;background:var(--lgray);font-size:4px;line-height:5px;text-align:center;color:#555;padding:3px}
.cover{background:var(--navy)}
.cover-art{position:absolute;left:100px;top:12px;width:170px;height:186px;border-radius:50%;background:radial-gradient(circle,#3a4a8a 40%,#5a66a0 60%,var(--navy) 72%)}
.cover-disc{position:absolute;left:125px;top:45px;width:120px;height:120px;border-radius:50%;background:#fff;text-align:center}
.cover-date{font-size:4.5px;margin-top:20px;color:#666}
.cover-name{font-size:9px;font-weight:700;color:#666;margin-top:20px;letter-spacing:.3px;border-bottom:.6px solid #999;padding-bottom:3px;margin-left:10px;margin-right:10px}
.cover-sub{font-size:5.5px;color:#666;margin-top:3px}
.index-title{position:absolute;left:34px;top:17px;font-size:9.5px;font-weight:500;color:#555}
.index-rule{position:absolute;left:34px;width:303px;top:29px;height:1px;background:#888}
.index-list{position:absolute;left:34px;top:41px;width:303px;list-style:none}
.index-list li{display:flex;justify-content:space-between;font-size:8px;line-height:15px}
.footer-brown{background:var(--brown)}
.c-title{position:absolute;left:34px;top:15px;font-size:9.5px;font-weight:500;color:var(--teal)}
.c-rule{position:absolute;left:34px;top:27px;width:303px;height:1px;background:var(--teal)}
.c-sub{position:absolute;left:34px;top:30px;font-size:7.3px;color:var(--teal)}
.wordmark{position:absolute;left:34px;top:52px;font-size:13px;font-weight:700;color:var(--blue)}
.footer-teal{background:var(--teal)}
.chapter{background:var(--olive)}
.chapter-title{position:absolute;left:34px;top:15px;font-size:9.5px;font-weight:500;color:#fff}
.chapter-rule{position:absolute;left:34px;top:27px;width:316px;height:.8px;background:#fff}
.chapter-art{position:absolute;left:80px;top:50px;width:230px;height:110px;border-radius:50% 40% 30% 30%;background:linear-gradient(120deg,#8a9a55,#6d7d3e)}
.chapter-line{position:absolute;left:0;top:169px;width:370px;height:1px;background:#fff}
.data-table{position:absolute;left:34px;top:46px;width:303px;border-collapse:collapse;font-size:4.1px;color:#555}
.data-table th{font-weight:500;text-align:left;font-size:4.6px;border-bottom:.8px solid #555;padding:1px 10px;line-height:4.6px}
.data-table td{padding:0 10px;height:6.9px;line-height:6.9px}
.data-table tr:nth-child(even) td{background:#ececec}
.data-table td.v,.data-table th.v{text-align:center}
.data-table tbody tr:last-child td{border-bottom:.8px solid #555}
.table-note{position:absolute;right:33px;top:170px;font-size:3.8px;line-height:4.6px;text-align:right;color:#666}
.tile{position:absolute;color:#fff;font-size:3.3px;line-height:3.8px;text-align:center;padding:1px 2px}
.tile b{display:block;font-size:5px;line-height:5.5px;font-weight:500}
.box-head{background:var(--olive);color:#fff;font-size:4.3px;padding:1px 3px}
.box-body{background:var(--lime-pale);font-size:3.4px;line-height:4.3px;color:#777;padding:2px 3px}
.ellipse{position:absolute;left:253px;top:117px;width:84px;height:58px;border-radius:50%;background:var(--olive);color:#fff;text-align:center;font-size:5.6px;line-height:6.4px;padding-top:10px}
.ellipse-key{display:flex;align-items:center;justify-content:center;gap:3px;margin-top:4px;font-size:4.4px;line-height:5px}
.ellipse-swatch{display:inline-block;width:14px;height:10px;border-radius:50%;background:var(--lime-pale)}
</style>
</head>
<body>

<section class="slide cover col-l row1">
  <div class="cover-art" role="img" aria-label="Ring of hand-drawn shoppers and shopping icons around a white disc"></div>
  <div class="cover-disc">
    <p class="cover-date">Aprile 2022</p>
    <p class="cover-name">RETAIL ONLINE</p>
    <p class="cover-sub">Gli acquisti digitali degli italiani</p>
  </div>
</section>

<section class="slide col-r row1">
  <h2 class="index-title">INDICE DEL DOCUMENTO</h2>
  <div class="index-rule"></div>
  <ul class="index-list">
    <li style="color:var(--olive-dark)"><span>Lo sviluppo del Retail Online in Italia</span><span>04</span></li>
    <li style="color:var(--blue)"><span>Il percorso verso l’acquisto</span><span>13</span></li>
    <li style="color:#b0245a"><span>I beni e servizi acquistati</span><span>19</span></li>
    <li style="color:var(--orange)"><span>Sistema di pagamento</span><span>24</span></li>
    <li style="color:#555"><span>Delivery &amp; download e soddisfazione</span><span>28</span></li>
    <li style="color:#2a8cc0"><span>Device utilizzato nell’acquisto online</span><span>32</span></li>
    <li style="color:var(--red)"><span>Le soluzioni digitali nei negozi fisici</span><span>35</span></li>
    <li style="color:var(--teal)"><span>Live streaming commerce</span><span>48</span></li>
    <li style="color:#555"><span>Note metodologiche</span><span>51</span></li>
  </ul>
  <div class="footer footer-brown" style="top:187px"><span>Retail Online - Aprile 2022</span><span>2</span></div>
</section>

<section class="slide col-l row2">
  <h2 class="c-title">VENDICOM</h2>
  <div class="c-rule"></div>
  <p class="c-sub">Il consorzio del Commercio Digitale Italiano</p>
  <div class="wordmark">Vendicom</div>
  <div class="abs body-text" style="left:120px;top:52px;width:74px">Vendicom, il Consorzio del Commercio Digitale Italiano, è l’associazione di riferimento del settore e-commerce in Italia e uno</div>
  <div class="abs body-text" style="left:34px;top:81px;width:152px">stakeholder chiave nel dialogo sull’evoluzione regolamentare del mercato digitale a livello nazionale ed europeo.<br><br>Vendicom riunisce circa 450 aziende, tra società internazionali e piccole e medie realtà di eccellenza e rappresenta oggi la più ampia comunità professionale del digitale in Italia, in grado di fornire una visione autorevole e anticipatrice delle evoluzioni generate dalle tecnologie sul mercato e sul fare impresa.<br><br>Dal 2005 il Consorzio mette a disposizione una piattaforma esclusiva di contenuti formativi, ricerche, casi e modelli di riferimento nel digitale.<br><br>Vendicom è tra i membri fondatori di Digital Trade Europe, l’Associazione Europea del Commercio Elettronico che coinvolge oltre 150.000 aziende in Europa.</div>
  <div class="abs body-text" style="left:194px;top:51px;width:143px">I principali ambiti nei quali Vendicom è impegnato riguardano: sviluppo di studi e ricerche sul mondo sul commercio digitale<br>• promozione di un palinsesto di <b>eventi</b> creando occasioni di approfondimento e di networking<br>• creazione di <b>gruppi di lavoro</b> che analizzano dal punto di vista economico e regolamentare le primarie industry del commercio digitale<br>• dialogo e rappresentanza presso le istituzioni italiane ed europee in materia di <b>regolamentazione del mercato digitale</b><br>• attività di comunicazione sul territorio nazionale<br>• affiancamento delle aziende associate tramite un <b>supporto legale, fiscale e servizi convenzionati</b><br>• progettazione e gestione di <b>percorsi formativi</b> focalizzati sui temi dell’e-commerce e della digital transformation<br>• sostegno all’<b>internazionalizzazione</b> delle aziende italiane e del Made in Italy<br>• diffusione delle competenze digitali nei cittadini italiani e la creazione di strumenti a sostegno degli acquisti online quali il <b>sigillo Vendicom</b>, che identifica i siti di e-commerce affidabili e di qualità.</div>
  <div class="footer footer-teal" style="top:187px"><span>Retail Online - Aprile 2022</span><span>3</span></div>
</section>

<section class="slide chapter col-r row2">
  <h2 class="chapter-title">LO SVILUPPO DELL’ECOMMERCE IN ITALIA</h2>
  <div class="chapter-rule"></div>
  <div class="chapter-art" role="img" aria-label="Line drawing of a child holding a slice of a large pie chart"></div>
  <div class="chapter-line"></div>
</section>

<section class="slide col-l row3">
  <h2 class="title">L’ECOMMERCE IN ITALIA</h2>
  <div class="title-rule"></div>
  <p class="subtitle">Dimensioni e trend</p>
  <table class="data-table">
    <thead><tr><th>Indicatore</th><th class="v">Valore</th><th class="v">Variaz pre pandemia</th></tr></thead>
    <tbody>
      <tr><td>Utenti Internet in Italia 15+ (settimanali)</td><td class="v">42,5 milioni</td><td class="v">+9,6%</td></tr>
      <tr><td>Acquirenti online tra utenti Internet</td><td class="v">77,8%</td><td class="v">+16,9 p.p.</td></tr>
      <tr><td>Acquirenti online nel trimestre</td><td class="v">33,3 milioni</td><td class="v">+40,2%</td></tr>
      <tr><td>Acquirenti online abituali (una volta al mese)</td><td class="v">23,9 milioni</td><td class="v">+44,7%</td></tr>
      <tr><td>Acquirenti online ogni 100 abitanti 18+</td><td class="v">66,0</td><td class="v">+40,2%</td></tr>
      <tr><td>Quota di acquirenti online uomini</td><td class="v">51,9%</td><td class="v">-0,6 p.p.</td></tr>
      <tr><td>Età media degli acquirenti online</td><td class="v">42,2 anni</td><td class="v">-0,8 anni</td></tr>
      <tr><td>Acquisti online nel trimestre</td><td class="v">127,9 milioni</td><td class="v">+45,7%</td></tr>
      <tr><td>Quota acquisti online da dispositivi mobili</td><td class="v">55,6%</td><td class="v">+10,2 p.p.</td></tr>
      <tr><td>Quota acquirenti online via App nel semestre</td><td class="v">57,2%</td><td class="v">+13,5 p.p.</td></tr>
      <tr><td>Valore mensile acquisti online nel 2021</td><td class="v">4.950 Mio €</td><td class="v">+33,1%</td></tr>
      <tr><td>Quota a valore degli acquisti di prodotti</td><td class="v">73,9%</td><td class="v">+20,8 p.p.</td></tr>
      <tr><td>Media acquisti online pro-capite nel trimestre</td><td class="v">3,83</td><td class="v">+3,9% Y/Y</td></tr>
      <tr><td>Valore acquisti online nel 2021</td><td class="v">51,8 B€</td><td class="v">+36,3% Y/Y</td></tr>
      <tr><td>Previsione valore acquisti online nel 2022</td><td class="v">56,4 B€</td><td class="v">+8,9% Y/Y</td></tr>
    </tbody>
  </table>
  <p class="table-note">Gli indicatori – se non diversamente indicato - si riferiscono al mese medio del primo trimestre 2022<br>La differenza rispetto al periodo pre-pandemico confronta i dati del 2019 con quelli del 2022</p>
  <div class="footer"><span>Retail Online - Aprile 2022</span><span>5</span></div>
</section>

<section class="slide col-r row3">
  <h2 class="title">L’ECOMMERCE IN ITALIA</h2>
  <div class="title-rule"></div>
  <p class="subtitle">Alcuni indicatori del fenomeno</p>
  <div class="tile" style="left:34px;top:44px;width:99px;height:20px;background:var(--olive)"><b>33,3 milioni</b>Acquirenti online negli ultimi tre mesi<br>(marzo 2022)</div>
  <div class="tile" style="left:34px;top:66px;width:99px;height:26px;background:var(--orange)"><b>+36,3%</b>Incremento di valore eCommerce rispetto al periodo pre-pandemia<br>(2022 su 2019)</div>
  <div class="tile" style="left:34px;top:94px;width:99px;height:23px;background:#3a9ad0"><b>31,5 milioni</b>Consegne medie mensili di prodotti acquistati online<br>(stima anno 2022)</div>
  <div class="tile" style="left:34px;top:119px;width:99px;height:30px;background:var(--lime)"><b>20,1%</b>Quota di acquirenti di sesso femminile negli acquisti online di Assicurazioni<br>(marzo 2022)</div>
  <div class="tile" style="left:34px;top:151px;width:99px;height:23px;background:var(--pink)"><b>4.700 M€</b>Valore mensile medio degli acquisti online degli italiani nel 2022<br>(marzo 2022)</div>
  <div class="tile" style="left:135px;top:44px;width:99px;height:28px;background:var(--dgray)"><b>78,6</b>Acquisti online di prodotti fisici ogni 100 acquisti online<br>(marzo 2022)</div>
  <div class="tile" style="left:135px;top:74px;width:99px;height:28px;background:var(--blue)"><b>57,2%</b>Quota di acquirenti online che negli ultimi sei mesi ha fatto acquisti via App sul dispositivo mobile<br>(marzo 2022)</div>
  <div class="tile" style="left:135px;top:104px;width:99px;height:26px;background:var(--mgray)"><b>14,0</b>Pacchi ritirati in un luogo fisico ogni 100 pacchi spediti per un acquisto online<br>(marzo 2022)</div>
  <div class="tile" style="left:237px;top:44px;width:99px;height:26px;background:var(--mgray)"><b>58,9 €</b>spesi online dalle donne ogni 100€ spesi online da tutti gli italiani<br>(marzo 2022)</div>
  <div class="tile" style="left:237px;top:72px;width:99px;height:21px;background:var(--olive)"><b>11,9 su 100</b>acquisti online presso merchant di retailer tradizionali<br>(marzo 2022)</div>
  <div class="tile" style="left:237px;top:95px;width:99px;height:35px;background:var(--orange)"><b>57</b>Età media degli acquirenti online di prodotti enogastronomici<br>(marzo 2022)<br>(Età media acquirenti online = 42,5)</div>
  <div class="tile" style="left:135px;top:132px;width:201px;height:12px;background:var(--red);text-align:left;display:flex;gap:14px;align-items:center"><span><b>54,9%</b>(marzo 2022)</span><span>Acquisti online presso un merchant sul quale si era già acquistato in passato</span></div>
  <div class="tile" style="left:135px;top:146px;width:99px;height:28px;background:var(--blue)"><b>50,1</b>Acquisti originati da Smartphone ogni 100 acquisti online<br>(marzo 2022)</div>
  <div class="tile" style="left:237px;top:146px;width:99px;height:28px;background:var(--teal)"><b>1,39 milioni</b>Consegne mensili in negozio di prodotti acquistati online dallo stesso retailer<br>(marzo 2022)</div>
  <div class="tile" style="left:34px;top:176px;width:302px;height:6px;background:var(--lime);color:#333;line-height:5px"><b style="display:inline;font-size:4.3px">3,6 pagamenti su 100</b> con Smartphone nei negozi dei top 271 retailer (marzo 2022)</div>
  <div class="footer" style="top:189px"><span>Retail Online - Aprile 2022</span><span>6</span></div>
</section>

<section class="slide col-l row4">
  <h2 class="title">LE DIMENSIONI DEL FENOMENO</h2>
  <div class="title-rule"></div>
  <p class="subtitle">La diffusione dell’esperienza di acquisto online in Italia</p>
  <svg class="abs" style="left:30px;top:50px" width="160" height="96" viewBox="0 0 160 96" font-family="Alegreya Sans, sans-serif" font-size="3.4" fill="#666">
    <g><text x="0" y="4">36</text><text x="0" y="12">32</text><text x="0" y="20">28</text><text x="0" y="28">24</text><text x="0" y="37">20</text><text x="0" y="45">16</text><text x="0" y="53">12</text><text x="2" y="62">8</text><text x="2" y="70">4</text><text x="2" y="78">0</text></g>
    <rect x="12" y="3" width="3" height="3" fill="var(--lime)"/><text x="17" y="6" fill="var(--olive)">Sporadici   9,6 milioni (+2,2M rispetto al 2019)</text>
    <rect x="12" y="10" width="3" height="3" fill="var(--olive)"/><text x="17" y="13" fill="var(--olive)">Abituali   23,9 milioni (+7,4M rispetto al 2019)</text>
    <g fill="var(--olive)">
      <rect x="10" y="67" width="9" height="11"/><rect x="23.5" y="66" width="9" height="12"/><rect x="37" y="63" width="9" height="15"/><rect x="50.5" y="61" width="9" height="17"/><rect x="64" y="57" width="9" height="21"/><rect x="77.5" y="55" width="9" height="23"/><rect x="91" y="53" width="9" height="25"/><rect x="104.5" y="51" width="9" height="27"/><rect x="118" y="44" width="9" height="34"/><rect x="131.5" y="38" width="9" height="40"/><rect x="145" y="29" width="9" height="49"/>
    </g>
    <g fill="var(--lime)">
      <rect x="10" y="60" width="9" height="7"/><rect x="23.5" y="57" width="9" height="9"/><rect x="37" y="53" width="9" height="10"/><rect x="50.5" y="50" width="9" height="11"/><rect x="64" y="46" width="9" height="11"/><rect x="77.5" y="43" width="9" height="12"/><rect x="91" y="41" width="9" height="12"/><rect x="104.5" y="38" width="9" height="13"/><rect x="118" y="31" width="9" height="13"/><rect x="131.5" y="25" width="9" height="13"/><rect x="145" y="18" width="9" height="11"/>
    </g>
    <line x1="9" y1="78" x2="156" y2="78" stroke="#888" stroke-width=".4"/>
    <g font-size="3" text-anchor="middle"><text x="14.5" y="84">2011</text><text x="28" y="84">2012</text><text x="41.5" y="84">2013</text><text x="55" y="84">2014</text><text x="68.5" y="84">2015</text><text x="82" y="84">2016</text><text x="95.5" y="84">2017</text><text x="109" y="84">2018</text><text x="122.5" y="84">2019</text><text x="136" y="84">2020</text><text x="149.5" y="84">2021</text></g>
  </svg>
  <div class="caption" style="left:34px;top:152px;width:152px;height:26px;font-size:4.6px;line-height:5.4px;font-weight:500">Milioni di acquirenti online nel trimestre, distinti tra sporadici e abituali: negli ultimi tre anni (dal periodo pre-pandemia) gli abituali sono cresciuti tre volte tanto gli sporadici</div>
  <div class="abs" style="left:203px;top:52px;width:72px">
    <div class="box-head">Le dimensioni dell’utenza Internet italiana</div>
    <div class="box-body" style="width:42px">In Italia 42,5 milioni di individui di almeno 15 anni di età accedono regolarmente alla Rete almeno una volta alla settimana, da ogni luogo e utilizzando un qualsiasi device.</div>
  </div>
  <svg class="abs" style="left:226px;top:85px" width="100" height="100" viewBox="0 0 100 100" font-family="Alegreya Sans, sans-serif" font-size="3.2" text-anchor="middle">
    <circle cx="46" cy="52" r="46" fill="#f1f2df"/>
    <circle cx="46" cy="62" r="35" fill="#d7dca6"/>
    <circle cx="46" cy="70" r="26" fill="var(--lime)"/>
    <circle cx="46" cy="77" r="18" fill="var(--olive)"/>
    <text x="46" y="16" font-weight="700" fill="#333">Universo</text><text x="46" y="20" font-weight="700" fill="#333">Internet italiano</text>
    <text x="46" y="34" fill="#333">Acquirenti online</text><text x="46" y="38" fill="#333">almeno una volta</text><text x="46" y="42" fill="#333">nella vita</text>
    <text x="46" y="54" fill="#fff">Acquirenti online</text><text x="46" y="58" fill="#fff">negli ultimi 3 mesi</text>
    <text x="46" y="77" fill="#fff">Acquirenti online</text><text x="46" y="81" fill="#fff">abituali</text>
  </svg>
  <div class="abs body-text" style="left:290px;top:78px;width:47px;text-align:right">Totale utenza Internet italiana 42,5 M di individui 15+</div>
  <div class="abs body-text" style="left:290px;top:112px;width:47px;text-align:right;color:#999">85,0% dell’utenza Internet ovvero 36,1M di individui</div>
  <div class="abs body-text" style="left:203px;top:141px;width:34px;text-align:left">78,4% dell’utenza pari a 33,3 M di individui</div>
  <div class="abs body-text" style="left:203px;top:172px;width:40px;text-align:left">56,4% dell’universo pari a 23,9 M individui</div>
  <div class="footer"><span>Retail Online - Aprile 2022</span><span>7</span></div>
</section>

<section class="slide col-r row4">
  <h2 class="title">LE DIMENSIONI DEL FENOMENO</h2>
  <div class="title-rule"></div>
  <p class="subtitle">Il numero di atti di acquisto online</p>
  <svg class="abs" style="left:30px;top:48px" width="150" height="90" viewBox="0 0 150 90" font-family="Alegreya Sans, sans-serif" font-size="3.4" fill="#666">
    <text x="0" y="4">140</text><text x="0" y="15">120</text><text x="0" y="26">100</text><text x="2" y="36">80</text><text x="2" y="47">60</text><text x="2" y="57">40</text><text x="2" y="68">20</text><text x="4" y="78">0</text>
    <g fill="var(--olive)">
      <rect x="12" y="64" width="6" height="14"/><rect x="20" y="61" width="6" height="17"/><rect x="28" y="58" width="6" height="20"/><rect x="36" y="56" width="6" height="22"/><rect x="44" y="52" width="6" height="26"/><rect x="52" y="51" width="6" height="27"/><rect x="60" y="47" width="6" height="31"/><rect x="68" y="42" width="6" height="36"/><rect x="76" y="35" width="6" height="43"/><rect x="84" y="32" width="6" height="46"/><rect x="92" y="21" width="6" height="57"/><rect x="100" y="10" width="6" height="68"/><rect x="108" y="9" width="6" height="69"/>
    </g>
    <line x1="11" y1="78" x2="116" y2="78" stroke="#888" stroke-width=".4"/>
    <g font-size="2.2" text-anchor="middle"><text x="15" y="84">2011</text><text x="23" y="84">2012</text><text x="31" y="84">2013</text><text x="39" y="84">2014</text><text x="47" y="84">2015</text><text x="55" y="84">2016</text><text x="63" y="84">2017</text><text x="71" y="84">2018</text><text x="79" y="84">2019</text><text x="87" y="84">2020</text><text x="95" y="84">2021</text><text x="103" y="84">2022</text><text x="111" y="84">2022</text></g>
  </svg>
  <svg class="abs" style="left:130px;top:68px" width="56" height="60" viewBox="0 0 56 60" font-family="Alegreya Sans, sans-serif" text-anchor="middle">
    <text x="28" y="8" font-size="6" fill="var(--olive)" transform="rotate(12 28 8)">Ultimi sei mesi</text>
    <circle cx="28" cy="36" r="22" fill="var(--lime)"/>
    <path d="M28 36 L28 14 A22 22 0 0 1 48.5 28 Z" fill="var(--olive)"/>
    <text x="38" y="24" font-size="2.6" fill="#fff">Beni digitali</text><text x="38" y="27" font-size="2.6" fill="#fff">21,4%</text>
    <text x="22" y="44" font-size="3" fill="#f4f4e0">Prodotti fisici</text><text x="22" y="48" font-size="3" fill="#f4f4e0">78,6%</text>
  </svg>
  <div class="caption" style="left:34px;top:144px;width:74px;height:28px;font-size:3.4px;line-height:4.2px">Numero di acquisti online nel trimestre (in milioni) generati da acquirenti italiani su siti in Italia e all’estero</div>
  <div class="abs" style="left:112px;top:144px;width:74px">
    <div class="box-head">Il numero di acquisti online</div>
    <div class="box-body">• 127 milioni di atti d’acquisto online nel I trimestre 2022<br>• +45,7% rispetto allo stesso periodo del 2019 (pre-pandemia)<br>• la quota di acquisti di prodotti prevale sui servizi quando fino al 2016 era prossima alla parità</div>
  </div>
  <div class="abs body-text" style="left:190px;top:46px;width:147px">Gli acquirenti online italiani hanno compiuto in media 1,3 acquisti al mese primo trimestre del 2022. Il numero di acquisti online cresce in modo costante e ha superato le 100 milioni di transazioni per trimestre nel 2020. La spinta della pandemia si è protratta fino al 2021 e ora si è esaurita. Ogni 100 acquisti online, negli anni 2014-2018 il circa 60 riguardavano prodotti fisici e 40 servizi e beni digitali. Il rapporto tra prodotti e servizi è cambiato notevolmente negli ultimi tre anni e ora si contano quasi 4 acquisti di prodotti per ogni acquisto di servizi e beni digitali. Il fenomeno è anche segnato da una chiara stagionalità.</div>
  <div class="abs body-text" style="left:190px;top:106px;width:48px">La frequenza di acquisto distingue tra acquirenti abituali, che acquistano almeno una volta al mese, e acquirenti sporadici, meno di tre acquisti nel trimestre. L’eCommerce è guidato dal segmento degli acquirenti abituali: 23,9 milioni di individui che generano la quasi totalità del valore dell’eCommerce italiano.</div>
  <div class="abs" style="left:241px;top:106px;width:96px">
    <div class="box-head">Gli acquisti sporadici (9,6 milioni)</div>
    <div class="box-body">• uno o due acquisti nel trimestre<br>• effettuano il 13% delle transazioni del trimestre<br>• scontrino medio del 29% inferiore alla media<br>• generano il 9% del valore totale degli acquisti</div>
    <div class="box-head" style="margin-top:3px">Gli acquisti abituali (23,9 milioni)</div>
    <div class="box-body">• tre o più acquisti nel trimestre<br>• effettuano l’89% delle transazioni del trimestre<br>• scontrino medio superiore alla media (+11%)<br>• generano il 91% del valore totale degli acquisti</div>
  </div>
  <div class="footer"><span>Retail Online - Aprile 2022</span><span>8</span></div>
</section>

<section class="slide col-l row5">
  <h2 class="title">IL VALORE DEGLI ACQUISTI ONLINE</h2>
  <div class="title-rule"></div>
  <p class="subtitle">Il valore degli acquisti online sviluppato dagli italiani</p>
  <svg class="abs" style="left:30px;top:60px" width="150" height="86" viewBox="0 0 150 86" font-family="Alegreya Sans, sans-serif" font-size="3.4" fill="#666">
    <text x="0" y="4">60</text><text x="0" y="16">50</text><text x="0" y="27">40</text><text x="0" y="39">30</text><text x="0" y="51">20</text><text x="0" y="62">10</text><text x="2" y="74">0</text>
    <g fill="var(--orange)">
      <rect x="10" y="62" width="9" height="10"/><rect x="21" y="60" width="9" height="12"/><rect x="33" y="59" width="9" height="13"/><rect x="44" y="55" width="9" height="17"/><rect x="56" y="52" width="9" height="20"/><rect x="67" y="48" width="9" height="24"/><rect x="79" y="44" width="9" height="28"/><rect x="90" y="36" width="9" height="36"/><rect x="102" y="29" width="9" height="43"/><rect x="113" y="26" width="9" height="46"/><rect x="125" y="16" width="9" height="56"/><rect x="136" y="5" width="9" height="67"/>
    </g>
    <line x1="9" y1="72" x2="147" y2="72" stroke="#888" stroke-width=".4"/>
    <g font-size="2.8" text-anchor="middle"><text x="14.5" y="79">2011</text><text x="25.5" y="79">2012</text><text x="37.5" y="79">2013</text><text x="48.5" y="79">2014</text><text x="60.5" y="79">2015</text><text x="71.5" y="79">2016</text><text x="83.5" y="79">2017</text><text x="94.5" y="79">2018</text><text x="106.5" y="79">2019</text><text x="117.5" y="79">2020</text><text x="129.5" y="79">2021</text><text x="140.5" y="79">2022</text></g>
  </svg>
  <div class="caption" style="left:42px;top:155px;width:127px;height:20px">Valore annuale (n Miliardi di Euro) degli acquisti online generati dagli acquirenti italiani presso Merchant italiani e stranieri</div>
  <div class="abs body-text" style="left:186px;top:46px;width:151px">Nel 2022 si prevede che il valore complessivo degli acquisti online generati dagli acquirenti online italiani raggiunga la cifra di <b>58 miliardi di euro.</b><br><br>La crescita del valore è stata costante dall’inizio delle rilevazioni, nel 2011, fino al 2019, intorno al 20% anno su anno. La pandemia ha generato una discontinuità e nel 2020 la crescita si è limitata a poco più del 3% sull’anno precedente.<br><br>Tuttavia, il dato del 2020 è una media che si ottiene dalla forte crescita dell’eCommerce di prodotti e la significativa riduzione di servizi e beni digitali, in particolare nel settore dei trasporti e del turismo.</div>
  <div class="abs body-text" style="left:186px;top:102px;width:72px">Il valore pro-capite annuale degli acquisti online ha seguito un profilo di sviluppo diverso negli anni: è cresciuto fra il 2012 e il 2019 e poi si è stabilizzato, dopo un calo di 10% nell’anno della pandemia causato dalla consistente riduzione degli acquisti nel settore del turismo.<br><br>La crescita dell’eCommerce è quindi da attribuire a due fattori: l’allargamento della base degli acquirenti e l’aumento di frequenza (abitudine) di acquisto online. La spesa media annuale degli acquirenti abituali è cinque volte quella degli sporadici.</div>
  <svg class="abs" style="left:262px;top:104px" width="78" height="64" viewBox="0 0 78 64" font-family="Alegreya Sans, sans-serif" font-size="3" fill="#666">
    <text x="0" y="4">2.000 €</text><text x="0" y="18">1.500 €</text><text x="0" y="32">1.000 €</text><text x="3" y="46">500 €</text><text x="8" y="56">0 €</text>
    <g fill="var(--yellow)">
      <rect x="14" y="30" width="3.4" height="25"/><rect x="19" y="29" width="3.4" height="26"/><rect x="24" y="28" width="3.4" height="27"/><rect x="29" y="27" width="3.4" height="28"/><rect x="34" y="24" width="3.4" height="31"/><rect x="39" y="20" width="3.4" height="35"/><rect x="44" y="16" width="3.4" height="39"/><rect x="49" y="12" width="3.4" height="43"/><rect x="54" y="9" width="3.4" height="46"/><rect x="59" y="13" width="3.4" height="42"/><rect x="64" y="11" width="3.4" height="44"/><rect x="69" y="11" width="3.4" height="44"/>
    </g>
    <line x1="13" y1="55" x2="75" y2="55" stroke="#888" stroke-width=".3"/>
    <g font-size="2.6" text-anchor="middle"><text x="16" y="61">2011</text><text x="31" y="61">2013</text><text x="46" y="61">2015</text><text x="56" y="61">2017</text><text x="66" y="61">2019</text><text x="73" y="61">2021</text></g>
  </svg>
  <div class="caption" style="left:263px;top:172px;width:74px;height:9px;padding:2px">Valore pro-capite degli acquisti online</div>
  <div class="footer" style="top:189px"><span>Retail Online - Aprile 2022</span><span>9</span></div>
</section>

<section class="slide col-r row5">
  <h2 class="title">VALORE E QUOTA DEGLI ACQUISTI ONLINE</h2>
  <div class="title-rule"></div>
  <p class="subtitle">Il contributo dell’online ai volumi complessivi del retail</p>
  <svg class="abs" style="left:30px;top:50px" width="106" height="84" viewBox="0 0 106 84" font-family="Alegreya Sans, sans-serif" font-size="3.2" fill="#666">
    <text x="0" y="4">60</text><text x="0" y="15">50</text><text x="0" y="26">40</text><text x="0" y="37">30</text><text x="0" y="48">20</text><text x="0" y="59">10</text><text x="2" y="70">0</text>
    <text x="88" y="4">60%</text><text x="88" y="18">48%</text><text x="88" y="31">36%</text><text x="88" y="45">24%</text><text x="88" y="58">12%</text><text x="88" y="70">0%</text>
    <g fill="var(--orange)">
      <rect x="8" y="60" width="5" height="9"/><rect x="14" y="58" width="5" height="11"/><rect x="20" y="57" width="5" height="12"/><rect x="26" y="54" width="5" height="15"/><rect x="32" y="51" width="5" height="18"/><rect x="38" y="47" width="5" height="22"/><rect x="44" y="43" width="5" height="26"/><rect x="50" y="35" width="5" height="34"/><rect x="56" y="28" width="5" height="41"/><rect x="62" y="25" width="5" height="44"/><rect x="68" y="15" width="5" height="54"/><rect x="74" y="6" width="5" height="63"/>
    </g>
    <polyline points="30,19 42,18 48,20 54,22 60,26 66,30 72,27 78,29" fill="none" stroke="#8a9a3a" stroke-width=".8"/>
    <line x1="7" y1="69" x2="82" y2="69" stroke="#888" stroke-width=".4"/>
    <g font-size="2.8" text-anchor="middle"><text x="10.5" y="76">2011</text><text x="22.5" y="76">2013</text><text x="34.5" y="76">2015</text><text x="46.5" y="76">2017</text><text x="58.5" y="76">2019</text><text x="70.5" y="76">2021</text></g>
  </svg>
  <svg class="abs" style="left:128px;top:73px" width="56" height="62" viewBox="0 0 56 62" font-family="Alegreya Sans, sans-serif" text-anchor="middle">
    <text x="28" y="8" font-size="6" fill="var(--olive)" transform="rotate(-12 28 8)">Ultimi sei mesi</text>
    <circle cx="28" cy="38" r="22" fill="var(--lime)"/>
    <path d="M28 38 L28 16 A22 22 0 0 1 49 44 Z" fill="var(--olive)"/>
    <text x="39" y="28" font-size="2.6" fill="#fff">Beni digitali</text><text x="39" y="31" font-size="2.6" fill="#fff">26,1%</text>
    <text x="20" y="46" font-size="3" fill="#f4f4e0">Prodotti fisici</text><text x="20" y="50" font-size="3" fill="#f4f4e0">73,9%</text>
  </svg>
  <div class="caption" style="left:34px;top:142px;width:70px;height:34px;font-size:3.4px;line-height:4.3px;padding-top:5px">Valore annuale (B€) dell’eCommerce generato dagli italiani (scala a sinistra) e quota di acquisti di servizi e beni digitali</div>
  <div class="abs" style="left:108px;top:142px;width:66px">
    <div class="box-head">Valore degli acquisti 2022</div>
    <div class="box-body">• 58 B€ nel 2022, tra i quali quasi tre su quattro per acquisti di prodotti<br>• crescita a valore all’8,9% Y/Y<br>• La spesa in prodotti guadagna quota rispetto ai servizi</div>
  </div>
  <div class="abs body-text" style="left:184px;top:46px;width:153px">Dall’inizio delle rilevazioni di Retail Online, il numero di acquisti online di prodotti è sempre stato superiore a quello per servizi e beni digitali. Tuttavia, lo scontrino medio più elevato nel caso di acquisti di servizi ha mantenuto fino al 2019 una quota in valore quasi pari tra le due categorie, con una leggera prevalenza dei prodotti.<br><br>Tale equilibrio è stato profondamente alterato dalla pandemia di Coronavirus. La domanda di prodotti è notevolmente aumentata nei mesi del primo lockdown (primavera 2020) e, allo stesso tempo, il blocco degli acquisti di viaggi e turismo ha influenzato negativamente la quota di servizi e beni digitali. Il risultato è un nuovo equilibrio che in termini di acquisti vede la quota di servizi ridotta a poco più del 21% e in termini di valore al 26%.</div>
  <div class="abs body-text" style="left:184px;top:121px;width:66px">In definitiva, la pandemia ha stimolato 9 miliardi in più di acquisti online e sei milioni di individui si sono attivati nell’eCommerce dal 2020 al 2022.</div>
  <div class="abs body-text" style="left:184px;top:141px;width:66px">La stima di valore dell’eCommerce per il 2022 indica che l’8% dei consumi delle famiglie italiane passerà quest’anno attraverso l’online. È un dato quasi doppio rispetto a quello del 2017: si può affermare che negli ultimi cinque anni è cambiata la struttura del retail italiano.</div>
  <div class="ellipse">Valore annuale dei<br>consumi delle famiglie<br>italiane: 700 B€
    <div class="ellipse-key"><span class="ellipse-swatch"></span>eCommerce: 58 B€</div>
  </div>
  <div class="footer" style="top:189px"><span>Retail Online - Aprile 2022</span><span>10</span></div>
</section>

</body>
</html>
```